New Business Card Design Project

The idea, the card is to put a card, which contains two companies at the same time. Please see the attached data and idea of how the current cards are.
Updates
VELDAK
Constructora
Ferrotrac Delmar SRL.
Equipos para Plantas de Tratamientos y Acueductos, Alquiler de Equipos Pesados para la Construcción.
C / Pedro Lucena No.47
Loma Clara, Santo Domingo. República Dominicana.
Tel .: 1809 555 4172
CEL: 1829 555 6281
teodoro@ferrotracdelmar.net
veldakobras@mailvista.example
www.ferrotracdelmar.net
Veldak construction.
Es una empresa constructora.
NOTA: La idea es llevar una sola tarjeta para dos compañías. o si no resulta hacer un diseño en cada lado, uno para cada empresa.Equipos para Plantas de Tratamiento y Acueductos, Alquiler de Equipos Pesados para la Construcción.
Deben de llevar, los logos.
VELDAK
Constructora
Ferrotrac Delmar SRL.
C / Pedro Lucena No.47
Tel .: 1809 555 4172
CEL: 1829 555 6281
Veldak construction.
VELDAK
Constructora
Ferrotrac Delmar SRL.
C / Pedro Lucena No.47
Tel .: 1809 555 4172
CEL: 1829 555 6281
Veldak construction.
It is a construction company
NOTE: The idea is to carry a single card for two companies. or if it does not turn out to make a design on each side, one for each company. Equipment for Treatment Plants and Aqueducts, Rental of Heavy Equipment for Construction.
They must carry, the logos.
How is the design similar to that, send example, for data, from previous designs.
What I'm looking for is a new design, not a remodeled copy
ferrotracdelmar
Tel: 1809 555 4172
cel: 1829 555 6281
teodoro@ferrotracdelmar.net
Direccion:
C/ Pedro Lucena # 47
Loma clara, Santo Domingo
Republica Dominicana
Veldak
constructora
Tel: 1809 555-3907
Cel: 1829 555 6281
veldaksa1@mailvista.example
Direccion:
C/ Pedro Lucena # 47
Republica Dominicana
Contact Information for Business Card
FERROTRAC DELMAR, S.R.L.
C/ Tomás Benítez Olarte esquina Pedro Lucena # 47
Loma Clara, Santo Domingo, República Dominicana
Office: 809.555.4172
Fax: 809.555.8364
Cel (Local): 829 555 6281
E-mail: DUMMY@DUMMY.com
E-mail:DUMMY@gmail.com
Website: http://www.DUMMY.com
Look and feel
Each slider illustrates characteristics of the customer's brand and the style your logo design should communicate.

```html
<!DOCTYPE html>
<html lang="es">
<head>
<meta charset="utf-8">
<title>Tarjetas Veldak / Ferrotrac Delmar</title>
<link rel="stylesheet" href="https://fonts.googleapis.com/css2?family=Montserrat:wght@700;800&family=Open+Sans:wght@400;600&display=swap">
<style>
  :root {
    --page-bg: #e4e4e6;
    --slate: #3e3e40;
    --slate-text: #d9d9d9;
    --slate-muted: #bdbdbd;
    --amber: #f4c21a;
    --orange: #e8601c;
    --navy: #0c4e8e;
    --ink: #2a2a2a;
    --paper: #ffffff;
    --mist: #e3ebf3;
  }
  * { box-sizing: border-box; margin: 0; padding: 0; }
  html, body { width: 1200px; height: 900px; overflow: hidden; }
  body {
    background: var(--page-bg);
    font-family: "Open Sans", Arial, sans-serif;
    position: relative;
  }
  .card {
    position: absolute;
    top: 295px;
    width: 540px;
    height: 310px;
    border-radius: 24px;
    overflow: hidden;
    box-shadow: 0 8px 22px rgba(0,0,0,0.18);
  }
  .card--veldak { left: 40px; background: var(--slate); color: var(--slate-text); }
  .card--ferrotrac { left: 620px; background: var(--paper); color: var(--ink); }

  /* shared contact block */
  .contact { position: absolute; list-style: none; font-size: 14px; line-height: 20px; }
  .contact li { display: flex; align-items: center; gap: 8px; }
  .contact svg { width: 13px; height: 13px; flex: none; }
  .address { position: absolute; text-align: right; font-size: 13px; line-height: 17px; }
  .holder-name { font-family: "Montserrat", Arial, sans-serif; font-weight: 800; font-size: 18px; letter-spacing: .3px; }
  .holder-role { font-size: 14px; }

  /* Veldak side */
  .veldak-brand { position: absolute; left: 42px; top: 88px; display: flex; align-items: center; gap: 14px; }
  .veldak-brand .mark { width: 46px; height: 46px; background: var(--orange); }
  .veldak-brand .name { font-family: "Montserrat", Arial, sans-serif; font-weight: 800; font-size: 54px; color: #e3e3e3; letter-spacing: 1px; line-height: 1; }
  .card--veldak .holder { position: absolute; left: 46px; top: 168px; }
  .card--veldak .holder-name { color: var(--amber); }
  .card--veldak .holder-role { color: var(--slate-muted); }
  .card--veldak .contact { left: 46px; top: 212px; color: var(--slate-text); }
  .card--veldak .contact svg { fill: var(--orange); }
  .card--veldak .address { right: 32px; top: 166px; color: var(--slate-muted); }

  /* Ferrotrac side */
  .globe-decor { position: absolute; right: -30px; top: -30px; width: 250px; height: 250px; border-radius: 50%;
    background: radial-gradient(circle at 45% 45%, #eef3f8 0%, var(--mist) 60%, rgba(227,235,243,0) 72%); }
  .ferro-brand { position: absolute; left: 28px; top: 34px; display: flex; align-items: center; gap: 16px; }
  .ferro-brand .mark { width: 72px; height: 72px; border-radius: 50%; border: 7px solid var(--amber); background: var(--navy); flex: none; }
  .ferro-brand .name { font-family: "Montserrat", Arial, sans-serif; font-weight: 800; font-size: 29px; line-height: 31px; color: var(--navy); }
  .card--ferrotrac .holder { position: absolute; left: 34px; top: 124px; }
  .card--ferrotrac .holder-name { color: var(--navy); }
  .card--ferrotrac .holder-role { color: var(--ink); }
  .card--ferrotrac .contact { left: 34px; top: 168px; color: var(--ink); font-size: 13.5px; line-height: 19px; }
  .card--ferrotrac .contact svg { fill: var(--navy); }
  .card--ferrotrac .address { right: 30px; top: 130px; color: var(--ink); }
  .tagline-band { position: absolute; left: 0; right: 0; bottom: 0; height: 62px; background: var(--navy);
    color: #fff; font-size: 13.5px; line-height: 18px; text-align: center; display: flex; align-items: center; justify-content: center; padding: 0 30px; }
</style>
</head>
<body>

<svg width="0" height="0" style="position:absolute">
  <defs>
    <symbol id="icon-phone" viewBox="0 0 16 16"><path d="M3.5 1.5l2.5 0 1 3.5-1.6 1.2a8 8 0 0 0 4.4 4.4l1.2-1.6 3.5 1v2.5c0 .8-.7 1.5-1.5 1.5A12.5 12.5 0 0 1 2 3c0-.8.7-1.5 1.5-1.5z"/></symbol>
    <symbol id="icon-mobile" viewBox="0 0 16 16"><path d="M2 2h12v12H2zM4 4v8h8V4z"/></symbol>
    <symbol id="icon-mail" viewBox="0 0 16 16"><path d="M1 3h14v10H1zM2.5 4.5v.4L8 8.8l5.5-3.9v-.4zM2.5 6.7v4.8h11V6.7L8 10.6z"/></symbol>
    <symbol id="icon-web" viewBox="0 0 16 16"><circle cx="8" cy="8" r="7"/></symbol>
  </defs>
</svg>

<section class="card card--veldak">
  <div class="veldak-brand">
    <span class="mark"></span>
    <span class="name">VELDAK</span>
  </div>
  <div class="holder">
    <p class="holder-name">LORUM SMITH</p>
    <p class="holder-role">Managing Director</p>
  </div>
  <ul class="contact">
    <li><svg><use href="#icon-phone"/></svg>809.555.4172</li>
    <li><svg><use href="#icon-mobile"/></svg>829 555 6281</li>
    <li><svg><use href="#icon-mail"/></svg>info@mailvista.example</li>
    <li><svg><use href="#icon-web"/></svg>www.ferrotracdelmar.net</li>
  </ul>
  <address class="address" style="font-style:normal">
    C/ Tomás Benítez Olarte<br>
    esquina Pedro Lucena # 47<br>
    Loma Clara, Santo Domingo<br>
    República Dominicana
  </address>
</section>

<section class="card card--ferrotrac">
  <div class="globe-decor" role="img" aria-label="Faint world globe decoration"></div>
  <div class="ferro-brand">
    <span class="mark"></span>
    <span class="name">FERROTRAC<br>DELMAR, S.R.L.</span>
  </div>
  <address class="address" style="font-style:normal">
    C/ Tomás Benítez Olarte<br>
    esquina Pedro Lucena # 47<br>
    Loma Clara, Santo Domingo<br>
    República Dominicana
  </address>
  <div class="holder">
    <p class="holder-name">LORUM SMITH</p>
    <p class="holder-role">Managing Director</p>
  </div>
  <ul class="contact">
    <li><svg><use href="#icon-phone"/></svg>809.555.4172</li>
    <li><svg><use href="#icon-mobile"/></svg>829 555 6281</li>
    <li><svg><use href="#icon-mail"/></svg>info@mailvista.example</li>
    <li><svg><use href="#icon-web"/></svg>www.ferrotracdelmar.net</li>
  </ul>
  <p class="tagline-band">Equipos para Plantas de Tratamientos y Acueductos, Rentas de<br>Equipos Pesados para la Construcción.</p>
</section>

</body>
</html>
```